Henri Marsac - Magician and Mentalist

I am a professional magician - mentalist based in Belgium. My stage name is Henri Marsac. I need a flyer (that I could use electronically or in print) to promote my activity. The flyer should represent myself "hand drawn" together with some classical attributes of a magician / mentalist : playing cards, billets, a crystal ball, some items related to mystery and conjuring... My logo has already been designed and I attach it enclosed. I also enclose a few pictures of me and a previous drawing that was made by a friend, but I am not satisfied with. As an example of what I like, I very much like the graphics of the poster of "Hollow Signals" (also enclosed). But it can be something totally different. See also my website for some graphic "feeling" : www.henrimarsac-demo.be

Target Market(s)

General public

Industry/Entity Type

Magician

Font styles to use
Other font styles liked:
• Old Newspaper Types (font enclosed in the uploaded files)

Colors

Designer to choose colors to be used in the design.

Requirements
Must have
• The project should reflect mystery/conjuring, and some items related to it (mainly playing cards but other elements may be inserted : a dice, ESP symbols, a "?" sign. Please see the enclosed files also.
Should not have
• I am not a "traditional" magician, so classic magic-related items like a hat, or a rabbit, or silks... should not appear in the design please.

```html
<!DOCTYPE html>
<html lang="fr">
<head>
<meta charset="utf-8">
<title>Henri Marsac – Mentaliste</title>
<link href="https://fonts.googleapis.com/css2?family=Old+Standard+TT:wght@400;700&display=swap" rel="stylesheet">
<style>
  :root {
    --ink-black: #070303;
    --deep-red: #4a0a06;
    --ember: #7a1a0c;
    --gold: #f3c566;
    --gold-soft: #eab857;
    --white: #ffffff;
  }
  html, body {
    margin: 0;
    padding: 0;
    width: 846px;
    height: 1200px;
    overflow: hidden;
    background: var(--ink-black);
  }
  .flyer {
    position: relative;
    width: 846px;
    height: 1200px;
    overflow: hidden;
    font-family: "Old Standard TT", "Times New Roman", serif;
    color: var(--gold);
  }
  .backdrop {
    position: absolute;
    inset: 0;
    background:
      radial-gradient(ellipse at 42% 40%, rgba(0,0,0,0.85) 0%, rgba(0,0,0,0.5) 18%, rgba(0,0,0,0) 42%),
      radial-gradient(ellipse at 30% 55%, var(--ember) 0%, var(--deep-red) 40%, var(--ink-black) 85%);
  }
  .brand-mark {
    position: absolute;
    left: 0;
    right: 0;
    top: 150px;
    text-align: center;
    font-weight: 700;
    font-size: 26px;
    letter-spacing: 1px;
    color: var(--gold);
  }
  .brand-mark .dot {
    display: inline-block;
    width: 12px;
    height: 12px;
    border-radius: 50%;
    background: var(--gold);
    margin-right: 10px;
    vertical-align: middle;
  }
  .headline {
    position: absolute;
    top: 254px;
    left: 0;
    right: 0;
    margin: 0;
    text-align: center;
    font-size: 31px;
    font-weight: 700;
    letter-spacing: 0.3px;
  }
  .intro {
    position: absolute;
    left: 50px;
    right: 50px;
    margin: 0;
    text-align: center;
    font-size: 20px;
    line-height: 26.5px;
    font-weight: 700;
  }
  .intro.first { top: 305px; }
  .intro.second { top: 490px; }
  .service {
    position: absolute;
    display: flex;
    align-items: center;
    font-size: 19px;
    line-height: 24px;
    font-weight: 700;
  }
  .service svg { flex: none; width: 30px; height: 30px; margin-right: 14px; }
  .service.reception { left: 76px; top: 615px; }
  .service.spectacle { left: 76px; top: 690px; }
  .service.entreprise { left: 474px; top: 617px; }
  .service.soiree { left: 474px; top: 682px; }
  .reviews-title {
    position: absolute;
    top: 775px;
    left: 194px;
    font-size: 24px;
    font-weight: 700;
    display: flex;
    align-items: center;
  }
  .reviews-title .stars { display: flex; gap: 14px; margin-left: 22px; }
  .reviews-title .stars svg { width: 26px; height: 26px; }
  .quotes {
    position: absolute;
    top: 832px;
    left: 0;
    right: 0;
    margin: 0;
    padding: 0;
    list-style: none;
    text-align: center;
    font-size: 18px;
    line-height: 30.5px;
    font-weight: 700;
    color: var(--white);
  }
  .contact-lead {
    position: absolute;
    top: 1016px;
    left: 0;
    right: 0;
    text-align: center;
    font-size: 19px;
    font-weight: 700;
    color: var(--gold-soft);
  }
  .contact-line {
    position: absolute;
    top: 1047px;
    left: 0;
    right: 0;
    text-align: center;
    font-size: 19px;
    font-weight: 700;
    color: var(--white);
    letter-spacing: 0.3px;
  }
  .contact-line .sep { margin: 0 12px; }
  .credentials {
    position: absolute;
    top: 1092px;
    left: 60px;
    right: 60px;
    margin: 0;
    text-align: center;
    font-size: 15px;
    line-height: 20px;
    font-weight: 700;
    color: var(--gold-soft);
  }
</style>
</head>
<body>
<div class="flyer">
  <div class="backdrop" role="img" aria-label="Fond décoratif : tourbillon de cartes à jouer rouge sombre sur noir"></div>

  <div class="brand-mark"><span class="dot"></span>Henri Marsac</div>

  <h1 class="headline">Henri Marsac lit dans vos pensées. Vraiment !</h1>

  <p class="intro first">Henri Marsac est un magicien spécialisé dans la discipline du mentalisme. Il devine vos pensées, prédit l’avenir et produit des miracles avec un simple jeu de cartes ou des objets d'une effarante banalité : dé, papier, marqueur, enveloppe, billet de banque, ... Il développe une magie très participative, qui permet aux spectateurs de réaliser, eux aussi, d'incroyables prouesses magiques et mentales.</p>

  <p class="intro second">Henri Marsac vous propose plusieurs formules « sur mesure » afin de coller parfaitement à vos souhaits. Donnez une touche incroyable et fantastique à votre prochain événement : invitez un mentaliste !</p>

  <div class="service reception">
    <svg viewBox="0 0 30 30" aria-hidden="true"><path d="M15 1 L27 15 L15 29 L3 15 Z" fill="#fff"/></svg>
    <span>Réception<br>(mariage, anniversaire, ...)</span>
  </div>
  <div class="service spectacle">
    <svg viewBox="0 0 30 30" aria-hidden="true"><path d="M15 2 C10 9 3 12 3 18 C3 22 7 24 11 22 C12 21 13 20 14 19 C14 23 12 26 9 28 L21 28 C18 26 16 23 16 19 C17 20 18 21 19 22 C23 24 27 22 27 18 C27 12 20 9 15 2 Z" fill="#fff"/></svg>
    <span>Spectacle</span>
  </div>
  <div class="service entreprise">
    <svg viewBox="0 0 30 30" aria-hidden="true"><circle cx="15" cy="8" r="6" fill="#fff"/><circle cx="8" cy="17" r="6" fill="#fff"/><circle cx="22" cy="17" r="6" fill="#fff"/><path d="M14 16 L16 16 Q16 25 20 28 L10 28 Q14 25 14 16 Z" fill="#fff"/></svg>
    <span>Evénement d’entreprise,<br>salon, foire</span>
  </div>
  <div class="service soiree">
    <svg viewBox="0 0 30 30" aria-hidden="true"><path d="M15 27 C9 21 2 17 2 10 C2 5 6 3 9 3 C12 3 14 5 15 7 C16 5 18 3 21 3 C24 3 28 5 28 10 C28 17 21 21 15 27 Z" fill="#fff"/></svg>
    <span>Soirée « mentalisme »<br>entre amis</span>
  </div>

  <div class="reviews-title">
    <span>Ce qu’ils en disent :</span>
    <span class="stars" aria-label="5 étoiles">
      <svg viewBox="0 0 24 24"><path d="M12 1 L15 9 L23 9 L16.5 14 L19 22 L12 17 L5 22 L7.5 14 L1 9 L9 9 Z" fill="#f3c566"/></svg>
      <svg viewBox="0 0 24 24"><path d="M12 1 L15 9 L23 9 L16.5 14 L19 22 L12 17 L5 22 L7.5 14 L1 9 L9 9 Z" fill="#f3c566"/></svg>
      <svg viewBox="0 0 24 24"><path d="M12 1 L15 9 L23 9 L16.5 14 L19 22 L12 17 L5 22 L7.5 14 L1 9 L9 9 Z" fill="#f3c566"/></svg>
      <svg viewBox="0 0 24 24"><path d="M12 1 L15 9 L23 9 L16.5 14 L19 22 L12 17 L5 22 L7.5 14 L1 9 L9 9 Z" fill="#f3c566"/></svg>
      <svg viewBox="0 0 24 24"><path d="M12 1 L15 9 L23 9 L16.5 14 L19 22 L12 17 L5 22 L7.5 14 L1 9 L9 9 Z" fill="#f3c566"/></svg>
    </span>
  </div>

  <ul class="quotes">
    <li>« Absolutely fantastic ! »</li>
    <li>« Vous avez séduit tous nos invités »</li>
    <li>« Tout simplement magistral ! »</li>
    <li>« Epoustouflant... »</li>
    <li>« Une fabuleuse expérience, merci !»</li>
  </ul>

  <div class="contact-lead">Pour toute information et demande de devis :</div>
  <div class="contact-line">www.henrimarsac-demo.be<span class="sep">|</span>info@henrimarsac-demo.be<span class="sep">|</span>(+)32 470 12 34 56</div>

  <p class="credentials">Henri Marsac est un magicien-mentaliste professionnel, membre de l’International Guild of Conjurers et de l'Open Circle of Magicians &amp; Mentalists (USA).</p>
</div>
</body>
</html>
```